Yoga/movement guide/teacher for adult yoga practice and kid yoga

What is the positioning or mission statement of your company? to guide individuals in a yoga-based safe and sustainable movement practice applicable to all ages and body types. Currently my focus is working with children in daycare and school settings, but my goal is to expand into private yoga practice for adults, and potentially as part of rented space in studios. I hope to find a way to work with children AND adults (so would love for logo to be appealing to both), but current focus is with children based on need and demand in the community. yoga for children also compliments my backround as a pediatrician/neonatologist, and I greatly miss interacting with children. I also want to emphasize a yoga/movement practice that is focused more on what one feels internally through movement. NOT what one looks like asthetically. I believe in removing all mirrors from yoga/movement practice. It should be an experience of movement/poses/yoga through appropriate cueing and education. It is not about the details of how far the knee should bend, or how high the leg should be. Focusing on foudation first, core, then core engagement and ultimately expression of poses/movements. A focus on strength, stability and mobility, not just flexibility, which is the common perception/association with yoga. I also want individuals to learn to be an advocate of their own health. Through guidance, I hope for individuals to connect with their body so they know themselves so well to be able to advocate for themselves in the modern healthcare world. This internal experience and connection is so essential in a world where modern medicine has become a business and it is all about making a dollar. the connection with patients is lost, and individuals need to learn to empower themselves and through their new found voice to be able to articulate what is wrong.<br/>Does your company have a tagline or slogan that should be included with the logo? "Practice Glowing Motion"<br/>What do you hope your company can be known for? Accessible yoga for a sustained practice. A guided movement practice where one gains information and knowledge of oneself through a mind/body connection. For one feel good physically with a new awaraness of their internal radiance that exists in all beings. Physical rejuvenation egnites a light and increases energy to flow through the physical body, which ultimately tranlates into works of kindness for others and out in the world. <br/>What color palettes might you prefer? why? love the colors currently chosen<br/>Where will the logo be primarily used? initially business cards, but hopefully future websites, t-shirts, and potentially local magazine adds. Also starting with a small couple of banners for community events in the area. I currently practice as a nomad out of my car :)<br/>Are there any elements you would prefer to see in the logo? Movement. A modern depiction of a human body/figure practicing movement. Hoping to avoid a stereotypical yoga pose per say, just because I want to people to think of it more of a movement practice with yoga roots. Modern yoga. There are elements of breathing and connecting with oneself through the flow of breath and movement, but I do not focus on the meditative/cerebral aspect of the yoga practice. What I teach is almost reaching a meditative state through movement. I personally don't practice, nor resonate with just seated meditation. just not my thing :)<br/>In your opinion, what defines a well-designed logo? curiosity. enough info for individuals to think they know what it means, but want to know more. invokes curiosity, but not too abstract. Reproducible. not too complicated. I want also to invoke a community feel, so a design that appeals to all people within a community. <br/>What is your preference in reference to icons, typography, spokespeople (characters), etc.? modern design. I love the idea of a logo for my purposes, to invoke a sense of movement from within. So not too static. <br/>What words or icons must be included in the logo? movement with yoga roots. <br/>What logos do you like and why? A representation, but not exact. I think some ambiguity is intriguing for others, and also memorable. I want it to be an artistic representation of movement/yoga<br/>What logos do you dislike and why? too busy, too loud. <br/>In your opinion, what is the primary purpose for a logo? association<br/>Who is the primary target audience? (who is most likely to use your services/product?) Children and their parents, but ultimately to expand into teaching adults. I even have aspirations of prenatal and post-natal yoga. Potentially incorporating infants. <br/>Who currently uses your product the most? n/a (working in schools/daycare currently. It is currently all volunteer)<br/>Are you pleased with the range of people your company serves? n/a<br/>Are you looking to expand, modify, or completely change your target audience? or will it remain the same? yes! expand into an adult audience. <br/>How do you plan to focus on your target audience? currently by working through schools and daycares. hopefully ultimately through after school care programs and then offering kid yoga in an existing yoga studio (working on this with Q Loft in Ridgeland, currently)<br/>What are your main forms of advertising? word of mouth, schools, daycares. Happy kids talking to their parents about the yoga class they took and happy teachers :)<br/>How do most customers find out about your company?<br/>Which gender are you targeting? All genders! However, with kid yoga, often the maternal individual in the child's life is more involved with decision making as far as extracurricular activities

Target Market(s)

individuals and families interested in wellness and feeling great

Contact Information for Business Card

Dana Whitmore
Yoga Instructor
RYT-200, RCYT

certified yoga teacher for adults and children

Colors

Designer to choose colors to be used in the design.

Requirements
Must have
• "Practice Glowing Motion"
Nice to have
• logo with same colors

```html
<!DOCTYPE html>
<html lang="en">
<head>
<meta charset="utf-8">
<title>Brightwell Studios – Business Card</title>
<link rel="stylesheet" href="https://fonts.googleapis.com/css2?family=Rokkitt:wght@400;600&display=swap">
<style>
  :root {
    --card-bg: #ffffff;
    --sun-yellow: #fcd84a;
    --ink-grey: #555555;
  }
  * { margin: 0; padding: 0; box-sizing: border-box; }
  html, body {
    width: 1200px;
    height: 686px;
    overflow: hidden;
    background: var(--card-bg);
  }
  .card {
    position: relative;
    width: 1200px;
    height: 686px;
    background: var(--card-bg);
    font-family: "Rokkitt", Georgia, serif;
    color: var(--ink-grey);
    overflow: hidden;
  }
  .ornament { position: absolute; display: block; }
  .ornament--top { left: 710px; top: 0; }
  .ornament--bottom { left: 29px; top: 456px; }

  .brand {
    position: absolute;
    left: 120px;
    top: 74px;
    width: 370px;
    height: 298px;
    display: flex;
    align-items: center;
    justify-content: center;
  }
  .brand__name {
    font-size: 46px;
    font-weight: 400;
    line-height: 1.1;
    text-align: center;
    color: var(--ink-grey);
  }

  .person__name {
    position: absolute;
    left: 556px;
    top: 296px;
    font-size: 56px;
    font-weight: 600;
    letter-spacing: 1px;
    line-height: 1.2;
    color: var(--ink-grey);
  }
  .contact {
    position: absolute;
    left: 566px;
    top: 418px;
    height: 207px;
    border-left: 4px solid var(--sun-yellow);
    list-style: none;
    padding-left: 26px;
    display: flex;
    flex-direction: column;
    justify-content: space-between;
  }
  .contact__item {
    display: flex;
    align-items: center;
    gap: 26px;
    font-size: 31px;
    letter-spacing: 0.5px;
    height: 44px;
    white-space: nowrap;
  }
  .contact__icon { width: 40px; height: 40px; flex: none; fill: var(--ink-grey); }
</style>
</head>
<body>
<main class="card">
  <svg class="ornament ornament--top" width="466" height="230" viewBox="0 0 466 230" role="img" aria-label="Yellow mandala ornament, upper half">
    <path d="M0 0 H466 A233 230 0 0 1 0 0 Z" fill="var(--sun-yellow)"/>
  </svg>
  <svg class="ornament ornament--bottom" width="464" height="232" viewBox="0 0 464 232" role="img" aria-label="Yellow mandala ornament, lower half">
    <path d="M0 232 A232 232 0 0 1 464 232 Z" fill="var(--sun-yellow)"/>
  </svg>

  <div class="brand">
    <span class="brand__name">Brightwell<br>Studios</span>
  </div>

  <h1 class="person__name">Dana Whitmore</h1>

  <ul class="contact">
    <li class="contact__item">
      <svg class="contact__icon" viewBox="0 0 24 24" aria-hidden="true">
        <path d="M6.6 10.8a15.1 15.1 0 0 0 6.6 6.6l2.2-2.2a1 1 0 0 1 1-.25 11.4 11.4 0 0 0 3.6.57 1 1 0 0 1 1 1V20a1 1 0 0 1-1 1A17 17 0 0 1 3 4a1 1 0 0 1 1-1h3.5a1 1 0 0 1 1 1c0 1.25.2 2.45.57 3.6a1 1 0 0 1-.25 1z"/>
      </svg>
      <span>+00 555 010 274</span>
    </li>
    <li class="contact__item">
      <svg class="contact__icon" viewBox="0 0 24 24" aria-hidden="true">
        <path d="M2 5h20v14H2z M3.5 6.5 12 13l8.5-6.5" fill="var(--ink-grey)" stroke="#fff" stroke-width="1.2"/>
      </svg>
      <span>info.brightwell@mailbox.com</span>
    </li>
    <li class="contact__item">
      <svg class="contact__icon" viewBox="0 0 24 24" aria-hidden="true">
        <circle cx="12" cy="12" r="9.5" fill="none" stroke="var(--ink-grey)" stroke-width="1.8"/>
        <rect x="1" y="9" width="22" height="6" fill="var(--ink-grey)"/>
        <text x="12" y="13.6" font-size="5" text-anchor="middle" fill="#fff" font-family="Arial, sans-serif" font-weight="700">www</text>
      </svg>
      <span>www.brightwellstudios.com</span>
    </li>
  </ul>
</main>
</body>
</html>
```